Postcard design to acquire new clients for my Property Management Company

I'm looking for a postcard design that I can send to prospective clients detailing information about my company and services.
Postcard should be eye catching and contain information from www.brightkeyrentals-example.com. I've provided a few screen shots for the most important information and my logo.
Target Market(s)
Real Estate
Industry/Entity Type
Real Estate
Font styles to use
Sans Serif
Requirements
Must have
- Must be eye catching!! this will be a direct mail piece - I'd like for the card to be read and not tossed in the trash immediately.
Design que from the logo.
A place to write / print the receipts name and address.
our physical address - 2287 Marble Lane, Lubbock, TX 79555.
Should not have
- the contact information on the business card is not accurate - please use info from website.

```html
<!DOCTYPE html>
<html lang="en">
<head>
<meta charset="utf-8">
<title>BrightKey Property Management – Postcard</title>
<link href="https://fonts.googleapis.com/css2?family=Roboto+Condensed:ital,wght@0,400;0,700;1,700&display=swap" rel="stylesheet">
<style>
  :root{
    --navy:#0d4b88;
    --navy-deep:#0a3f74;
    --ink:#1e3b63;
    --gray:#8e9194;
    --gray-dark:#6f7577;
    --gold:#f7b718;
    --gold-text:#f5b41a;
    --white:#ffffff;
    --line:#a9adb1;
    --stamp:#dde9f6;
    --green-ink:#1f3a2b;
  }
  *{box-sizing:border-box;margin:0;padding:0}
  html,body{width:800px;height:1200px;overflow:hidden;background:var(--white)}
  body{position:relative;font-family:"Roboto Condensed",Arial,sans-serif;color:var(--white)}
  .card{position:absolute;left:26px;width:750px;height:485px;overflow:hidden;box-shadow:6px 8px 10px rgba(0,0,0,.35)}
  .card--front{top:78px}
  .card--back{top:604px}
  .card svg.bg{position:absolute;inset:0;width:750px;height:485px}
  .t{position:absolute;white-space:nowrap}

  /* front */
  .brand{left:40px;top:52px;color:var(--ink);font-weight:700;line-height:1}
  .brand__name{font-size:34px;letter-spacing:5px}
  .brand__sub{font-size:14px;letter-spacing:3.2px;margin-top:4px}
  .front-banner{left:324px;top:52px;width:426px;height:41px;line-height:41px;text-align:center;font-weight:700;font-size:17px;padding-left:14px}
  .tagline{left:400px;top:102px;width:300px;text-align:center;font-size:16.5px;line-height:20px}
  .services-title{left:449px;top:162px;font-weight:700;font-size:23px;color:var(--gold-text);letter-spacing:.3px}
  .services{position:absolute;left:450px;top:196px;list-style:none}
  .services li{display:flex;align-items:center;height:25.4px;font-size:13px}
  .services svg{width:15px;height:15px;margin-right:9px;flex:none}
  .services span{display:block;width:214px;border-bottom:1px solid rgba(255,255,255,.35);padding:4px 0 5px 2px}
  .front-talk{left:30px;top:425px;font-size:14.5px;line-height:21px}
  .front-visit{left:438px;top:427px;font-size:12.5px;font-weight:700;color:var(--green-ink)}
  .front-web{left:438px;top:444px;font-size:17px;font-weight:700;letter-spacing:1.6px;color:var(--ink)}

  /* back */
  .back-banner{left:37px;top:33px;font-weight:700;font-style:italic;font-size:18px;line-height:22px}
  .back-head{left:38px;top:128px;font-weight:700;font-size:17.5px;line-height:22px}
  .back-copy{left:38px;top:184px;font-size:14px;line-height:17.4px}
  .back-copy p + p{margin-top:17.4px}
  .back-phone{left:37px;top:380px;font-size:34px;line-height:40px}
  .back-web{left:40px;top:427px;font-size:15.5px;font-weight:700;letter-spacing:2px}
  .back-address{left:40px;top:452px;font-size:13px}
  .offer{left:347px;top:22px;width:252px;text-align:center;color:var(--navy-deep)}
  .offer__big{font-size:40px;font-weight:700;line-height:40px}
  .offer__small{font-size:20px;font-weight:700;line-height:22px;margin-top:1px}
  .offer-list{position:absolute;left:390px;top:92px;list-style:none;color:var(--navy-deep);font-size:11.6px;line-height:14.4px;text-transform:uppercase}
  .offer-list li{position:relative;padding-left:15px;margin-bottom:7px}
  .offer-list li::before{content:"";position:absolute;left:0;top:3px;width:9px;height:9px;border-radius:50%;background:#0f2b22}
</style>
</head>
<body>

<section class="card card--front">
  <svg class="bg" viewBox="0 0 750 485">
    <defs>
      <linearGradient id="paper" x1="0" y1="0" x2="1" y2="1">
        <stop offset="0" stop-color="#ffffff"/><stop offset="1" stop-color="#e7ebef"/>
      </linearGradient>
      <linearGradient id="team" x1="0" y1="0" x2="1" y2="1">
        <stop offset="0" stop-color="#d9d2cb"/><stop offset=".5" stop-color="#9a9a9e"/><stop offset="1" stop-color="#4a4d55"/>
      </linearGradient>
      <linearGradient id="blueFront" x1="0" y1="0" x2="1" y2="1">
        <stop offset="0" stop-color="#0c4a86"/><stop offset="1" stop-color="#0f5597"/>
      </linearGradient>
    </defs>
    <rect width="750" height="485" fill="url(#paper)"/>
    <path d="M0 175 C120 160 280 170 410 175 V421 H0 Z" fill="url(#team)" role="img" aria-label="Photo of the smiling property management team giving thumbs up"/>
    <path d="M286 0 H750 V421 H334 C360 380 378 330 390 260 C410 170 360 60 286 0 Z" fill="url(#blueFront)" role="img" aria-label="Faint photo of Lubbock homes tinted blue"/>
    <rect x="324" y="52" width="426" height="41" fill="var(--gray)" opacity=".92"/>
    <polygon points="304,52 324,52 350,93 328,93" fill="var(--gray)" opacity=".92"/>
    <polygon points="0,421 334,421 270,485 0,485" fill="var(--navy)"/>
    <polygon points="334,421 750,421 750,485 270,485" fill="#a6a8aa"/>
  </svg>

  <div class="t brand">
    <div class="brand__name">BRIGHTKEY</div>
    <div class="brand__sub">PROPERTY MANAGEMENT</div>
  </div>

  <div class="t front-banner">PROPERTY MANAGEMENT ACROSS LUBBOCK, TX</div>
  <div class="t tagline">Maximize your financial returns with<br>support from our rental specialists</div>
  <div class="t services-title">DISCOVER OUR SERVICES</div>

  <ul class="services">
    <li><svg viewBox="0 0 16 16"><path d="M8 2 L15 8 H13 V14 H10 V10 H6 V14 H3 V8 H1 Z" fill="#fff"/></svg><span>Property Marketing</span></li>
    <li><svg viewBox="0 0 16 16"><circle cx="5.5" cy="5" r="2.6" fill="#fff"/><circle cx="11" cy="5.5" r="2.2" fill="#fff"/><path d="M1 13 C1 9 10 9 10 13 Z M9 13 C9 10 15 9.5 15 13 Z" fill="#fff"/></svg><span>Tenant Screening</span></li>
    <li><svg viewBox="0 0 16 16"><text x="8" y="13" text-anchor="middle" font-size="14" font-weight="700" fill="#fff" font-family="Arial,sans-serif">$</text></svg><span>Rent Collection</span></li>
    <li><svg viewBox="0 0 16 16"><path d="M2 14 L9 7" stroke="#fff" stroke-width="2.2" stroke-linecap="round"/><path d="M8 4 L11 1 L15 5 L12 8 Z" fill="#fff"/></svg><span>Maintenance</span></li>
    <li><svg viewBox="0 0 16 16"><circle cx="6.5" cy="6.5" r="4.3" fill="none" stroke="#fff" stroke-width="2"/><path d="M10 10 L14.5 14.5" stroke="#fff" stroke-width="2.4" stroke-linecap="round"/></svg><span>Property Inspections</span></li>
    <li><svg viewBox="0 0 16 16"><path d="M1.5 2 V14 H15" stroke="#fff" stroke-width="1.4" fill="none"/><path d="M5 12 V8 M8 12 V6 M11 12 V9 M13.5 12 V5" stroke="#fff" stroke-width="1.6"/></svg><span>Financial Reporting</span></li>
    <li><svg viewBox="0 0 16 16"><path d="M8 1 L14 3.5 V8 C14 11.5 11 14 8 15 C5 14 2 11.5 2 8 V3.5 Z" fill="#fff"/><path d="M8 3 V13 C10 12 12 10.5 12 8 V4.8 Z" fill="#0c4a86"/></svg><span>Evictions</span></li>
    <li><svg viewBox="0 0 16 16"><path d="M8 2 V14 M4 14 H12 M2 4 H14" stroke="#fff" stroke-width="1.4"/><path d="M2 4 L0.5 9 H3.5 Z M14 4 L12.5 9 H15.5 Z" fill="#fff"/></svg><span>Legal Guidance</span></li>
  </ul>

  <div class="t front-talk">Talk to Us About Your Rental Property<br>(806) 555-0147 &nbsp;-&nbsp; Realtor Referral Program</div>
  <div class="t front-visit">For more detial visit our site</div>
  <div class="t front-web">www.brightkeyrentals-example.com</div>
</section>

<section class="card card--back">
  <svg class="bg" viewBox="0 0 750 485">
    <defs>
      <radialGradient id="sky" cx="0.85" cy="0.1" r="1">
        <stop offset="0" stop-color="#cfe8f5"/><stop offset=".45" stop-color="#f1f9fd"/><stop offset="1" stop-color="#ffffff"/>
      </radialGradient>
      <radialGradient id="keys" cx="0.4" cy="0.35" r="0.7">
        <stop offset="0" stop-color="#ffffff"/><stop offset=".6" stop-color="#dcdfe2"/><stop offset="1" stop-color="#a9aeb3"/>
      </radialGradient>
    </defs>
    <rect width="750" height="485" fill="url(#sky)"/>
    <path d="M0 0 H580 C540 120 515 185 480 255 L440 330 C400 420 320 465 238 485 H0 Z" fill="var(--navy)"/>
    <rect x="0" y="20" width="374" height="86" fill="var(--gray-dark)"/>
    <circle cx="473" cy="100" r="126" fill="var(--gold)"/>
    <circle cx="410" cy="312" r="84" fill="var(--navy)"/>
    <circle cx="410" cy="312" r="74" fill="url(#keys)" role="img" aria-label="Photo of a silver house key with a house-shaped keychain"/>
    <rect x="638" y="19" width="92" height="90" fill="var(--stamp)" opacity=".85"/>
    <g stroke="var(--line)" stroke-width="1.3">
      <line x1="519" y1="252" x2="732" y2="252"/>
      <line x1="519" y1="290" x2="732" y2="290"/>
      <line x1="519" y1="326" x2="732" y2="326"/>
      <line x1="519" y1="364" x2="732" y2="364"/>
      <line x1="519" y1="396" x2="732" y2="396"/>
    </g>
  </svg>

  <div class="t back-banner">WE'RE THE LUBBOCK<br>PROPERTY MANAGEMENT<br>PROFESSIONALS</div>
  <div class="t back-head">When it comes to Texas rental homes,<br>we know what it takes to succeed.</div>
  <div class="t back-copy">
    <p>Don't settle for just anyone handling the needs of<br>your rental property in Lubbock. You need a<br>proven expert on your side who can handle all of<br>your home's needs. From property marketing and<br>tenant screening to maintenance coordination,<br>accounting support, and emergency response<br>services, we do it all.</p>
    <p>Learn more about our property management<br>packages today or call us to schedule a<br>free consultation now.</p>
  </div>
  <div class="t back-phone">(806) 555-0147</div>
  <div class="t back-web">www.brightkeyrentals-example.com</div>
  <div class="t back-address">2287 Marble Lane, Lubbock, TX 79555</div>

  <div class="t offer">
    <div class="offer__big">GET A FREE</div>
    <div class="offer__small">RENTAL ANALYSIS</div>
  </div>
  <ul class="offer-list">
    <li>Determine the rental value<br>of your property.</li>
    <li>Find out how to get the most<br>out of your investment.</li>
    <li>See if your home fits our<br>management approach.</li>
  </ul>
</section>

</body>
</html>
```